Revamp Current Website From 2012 TO 2018

We need a ravamp to our current website. I prefer a professional corporate modern feel to it.

My Current Website is www.brightlanepromoworks.biz. Please redesign the homepage and the /certs page first....see attached document for specific instructions..

There is a lot of content at the bottom but maybe we can shorten that by using titles and a pop up of the details or something so it doesnt take too mcuh space...or maybe a red more hyperlink to see the rest of info in pop up or something or new page...

Target Market(s)

B2B, business owners, website owners, marketing companies.

Industry/Entity Type

Promotional Product

Number of Pages Required

2 page

Colors

Designer to choose colors to be used in the design.

Requirements
Must have
• Please keep in mind logo mock up I am working on that looks beautiful on dark background for header...see attached for logo
• Must use existing content I hope your marketing mind comes in to play when designing the website.
• Must have all my content provided on each page...
Nice to have
• similiar color scheme...
Should not have
• I dont like using templates because usually hard to expand on design in future so Prefer full custom designs
• Please no templates

```html
<!DOCTYPE html>
<html lang="en">
<head>
<meta charset="utf-8">
<title>Brightlane Promoworks — Home</title>
<link href="https://fonts.googleapis.com/css2?family=Raleway:wght@300;400;600;700&display=swap" rel="stylesheet">
<style>
:root{
  --ink:#141414;
  --blue:#0a4bd6;
  --blue-deep:#0838c4;
  --link:#2f8df0;
  --navy:#0c1b44;
  --footer:#0a1122;
  --mist:#f3f4f7;
  --text:#4a4f5a;
  --muted:#8a8f99;
  --white:#ffffff;
}
*{margin:0;padding:0;box-sizing:border-box}
html,body{width:1200px;height:1200px;overflow:hidden;background:var(--white)}
body{font-family:'Raleway',sans-serif;position:relative}
.page{position:absolute;left:427.2px;top:0;width:431px;height:1500px;transform:scale(.8);transform-origin:0 0;overflow:hidden;background:var(--white)}
.abs{position:absolute}
section,header,footer{position:absolute;left:0;width:431px;overflow:hidden}

/* header */
.site-header{top:0;height:30px;background:var(--ink)}
.brand{left:35px;top:10px;display:flex;align-items:center;gap:4px;color:var(--link);font-weight:700;font-size:6.5px;letter-spacing:.3px;text-transform:uppercase}
.brand-mark{width:8px;height:8px;border-radius:50%;background:var(--link)}
.nav{top:12px;font-size:4px;color:#b9bcc4}
.nav.active{color:var(--link)}

/* hero */
.hero{top:30px;height:183px;background:linear-gradient(100deg,#2c3ad6 0%,#4b47d0 35%,#8a5fb8 65%,#cf8a94 100%)}
.hero-photo{left:0;top:0;width:431px;height:183px;background:radial-gradient(ellipse at 70% 45%,rgba(255,220,230,.35),rgba(40,40,120,0) 60%)}
.hero-contact{left:36px;top:5px;font-size:3.8px;color:var(--white)}
.hero-title{left:35px;top:59px;font-size:12px;font-weight:300;line-height:14.5px;color:#eef0ff}
.btn{position:absolute;height:12px;font-size:3.6px;display:flex;align-items:center;justify-content:center;border-radius:1px}
.btn-light{background:var(--white);color:var(--blue)}
.btn-solid{background:var(--blue);color:var(--white)}

/* stats */
.stats{top:213px;height:64px;background:var(--mist)}
.stat{top:18px;width:90px;text-align:center}
.stat-num{font-size:14px;font-weight:300;color:var(--blue)}
.stat-label{font-size:4.2px;color:var(--muted);margin-top:4px}

/* sunset */
.sunset{top:277px;height:179px;background:linear-gradient(180deg,#1d2a52 0%,#5a4a6a 28%,#d9804a 46%,#7a4a6a 60%,#3a2b52 100%)}
.sunset-copy{left:187px;top:45px;width:212px;color:var(--white)}
.sunset-copy h2{font-size:8px;font-weight:300;line-height:10.5px}
.small{font-size:3.8px;line-height:5.2px}

/* plug in */
.plug{top:456px;height:187px;background:linear-gradient(90deg,#ffffff,#f3f4f6)}
.plug h2{position:absolute;left:36px;top:31px;font-size:8px;font-weight:300;color:var(--text)}
.plug-col{width:120px}
.plug-col h3{font-size:5.5px;font-weight:700;color:var(--link);margin-bottom:5px}
.plug-col p{font-size:3.7px;line-height:5.2px;color:var(--muted)}
.phone-photo{left:316px;top:14px;width:75px;height:173px;border-radius:10px 10px 0 0;background:linear-gradient(160deg,#e9eaec,#c9cbd0 30%,#2a1d2a 38%,#c0512a 60%,#1d1320 100%)}

/* distribution */
.dist{top:643px;height:124px;background:linear-gradient(90deg,#0a37c0,#0a4bd6 50%,#0a3ec8)}
.dist h2{position:absolute;width:431px;top:17px;text-align:center;font-size:8px;font-weight:300;color:var(--white)}
.dist-item{top:45px;width:82px;text-align:center;color:var(--white)}
.dist-item svg{display:block;margin:0 auto;width:22px;height:22px}
.dist-item h3{font-size:4.6px;font-weight:700;margin-top:6px}
.dist-item p{font-size:3.6px;line-height:5px;margin-top:5px;color:#dfe6ff}

/* gift */
.gift{top:767px;height:179px;background:linear-gradient(95deg,#0b1a30 0%,#15243a 45%,#2a241e 75%,#1a1411 100%)}
.gift-photo{left:230px;top:0;width:201px;height:179px;background:radial-gradient(ellipse at 65% 45%,rgba(40,170,170,.35),rgba(0,0,0,0) 55%)}
.gift-copy{left:35px;top:56px;width:230px;color:var(--white)}
.gift-copy h2{font-size:8.5px;font-weight:300;line-height:11px}
.link{color:var(--link);font-size:3.8px}

/* feature cards */
.cards{top:946px;height:194px;background:#161616}
.card{top:21px;width:115px;height:150px;overflow:hidden}
.card svg{position:absolute;left:0;top:0}
.card-text{position:absolute;left:8px;width:99px;text-align:center;color:var(--white)}
.card-text h3{font-size:4.2px;font-weight:700;line-height:5.4px}
.card-text p{font-size:3.6px;line-height:5px;margin-top:5px}

/* call section */
.call{top:1140px;height:187px;background:linear-gradient(90deg,#eceef0,#f7f7f8 60%,#e8e9ec)}
.call-photo{left:60px;top:8px;width:68px;height:175px;border-radius:30px;background:linear-gradient(180deg,#e8463e,#d6322c 50%,#e8463e);opacity:.9}
.call-copy{right:39px;top:80px;text-align:right;color:var(--muted)}
.call-copy h2{font-size:8px;font-weight:300;line-height:11px}
.call-links{margin-top:8px;display:flex;gap:9px;justify-content:flex-end}

/* reseller */
.reseller{top:1327px;height:70px;background:var(--navy)}
.reseller-copy{left:35px;top:19px;color:var(--white)}
.reseller-copy h2{font-size:8.5px;font-weight:300;line-height:11px}

/* footer */
.site-footer{top:1397px;height:103px;background:var(--footer)}
.f-col{top:19px;font-size:3.8px;line-height:7.6px;color:#8c93a6}
.f-icon{display:inline-block;width:3.5px;height:3.5px;background:#8c93a6;margin-right:3px;vertical-align:middle}
.copyright{left:0;width:431px;top:90px;text-align:center;font-size:3.4px;color:#5d6478}
</style>
</head>
<body>
<div class="page">

  <header class="site-header">
    <div class="abs brand"><span class="brand-mark"></span>Brightlane Promoworks</div>
    <span class="abs nav active" style="left:158px">Home</span>
    <span class="abs nav" style="left:184px">Our Incentives</span>
    <span class="abs nav" style="left:226px">Sample</span>
    <span class="abs nav" style="left:254px">How it works</span>
    <span class="abs nav" style="left:293px">Testimonials</span>
    <span class="abs nav" style="left:332px">FAQ</span>
    <span class="abs nav" style="left:354px">Contact</span>
    <span class="abs nav" style="left:384px">Login</span>
  </header>

  <section class="hero">
    <div class="abs hero-photo" role="img" aria-label="Business man reviewing charts on a tablet"></div>
    <div class="abs hero-contact">&#9742; International: 1-800-555-0142 &nbsp; &#9742; USA: 555-010-7731</div>
    <h1 class="abs hero-title">Unlimited Incentives<br>For $99 Monthly - No Contracts<br>30 Day Risk Free Trial</h1>
    <a class="btn btn-light" style="left:35px;top:114px;width:46px">Learn More</a>
    <a class="btn btn-solid" style="left:83px;top:114px;width:88px">Sign Up Risk free for 30 days!</a>
  </section>

  <section class="stats">
    <div class="abs stat" style="left:29px"><div class="stat-num">4</div><div class="stat-label">Years In Business</div></div>
    <div class="abs stat" style="left:118px"><div class="stat-num">13,000+</div><div class="stat-label">Clients Enrolled</div></div>
    <div class="abs stat" style="left:210px"><div class="stat-num">2</div><div class="stat-label">Million Certificates In Circulation</div></div>
    <div class="abs stat" style="left:300px"><div class="stat-num">170,000+</div><div class="stat-label">Redemptions To Date</div></div>
  </section>

  <section class="sunset" role="img" aria-label="Airplane wing above clouds at sunset">
    <div class="abs sunset-copy">
      <h2>Increase Leads &amp; Sales From Your Existing Marketing Efforts By Offering High Perceived Value Incentives To Your Customers!</h2>
      <p class="small" style="margin-top:6px">Create a variety giveaway promotions for your business with an unlimited supply of top quality vacation getaway certificates, restaurant gift certificates, electronic product giveaways and gas or grocery rewards for just $99/mth.</p>
      <p class="small" style="margin-top:3px;font-weight:700">Whether you need 100 or 100,000 you will never pay more than $99.</p>
      <a class="btn btn-light" style="position:relative;margin-top:7px;width:46px">Learn More</a>
    </div>
  </section>

  <section class="plug">
    <h2>We plug right into your existing business model in 4 ways</h2>
    <div class="abs plug-col" style="left:36px;top:58px"><h3>Advertising</h3><p>Boost response rates from your existing ads by adding one extra tagline: "Call for a Free Quote and receive a Three Day Two Night Hotel Stay Certificate to a top city or 50 + other popular destinations, No Purchase Necessary" Imagine how many more leads you could generate.</p></div>
    <div class="abs plug-col" style="left:168px;top:58px"><h3>Residual Business</h3><p>Remind past clients about your products &amp; services with a 3 Night Hotel stay of your choice. Reach previous business clients using a personal touch and an incentive to book.</p></div>
    <div class="abs plug-col" style="left:36px;top:109px"><h3>Sales</h3><p>Now that you have generated the lead, try enticing a prospect with an upgrade and offer them Two Nights Plus Airfare if they purchase today. There are so many ways to clinch a deal by offering our incentives as a reward in your closing question.</p></div>
    <div class="abs plug-col" style="left:168px;top:109px"><h3>Referrals</h3><p>Contact all of your past customers and offer a Deluxe Vacation Package to anyone who fulfills your request for a new referral. Or, at the end of your sales presentation, offer you have achieved the sale, seduce new clients with a tempting perk if they send you a referral.</p></div>
    <div class="abs phone-photo" role="img" aria-label="Smartphone showing a city vacation certificate"></div>
  </section>

  <section class="dist">
    <h2>Easy Distribution</h2>
    <div class="abs dist-item" style="left:36px">
      <svg viewBox="0 0 24 24" fill="#fff"><rect x="7" y="2" width="10" height="6"/><rect x="2" y="8" width="20" height="9" rx="1"/><rect x="6" y="13" width="12" height="9" fill="#fff" stroke="#0a4bd6" stroke-width="1"/><rect x="8" y="15.5" width="8" height="1" fill="#0a4bd6"/><rect x="8" y="18" width="8" height="1" fill="#0a4bd6"/></svg>
      <h3>Print</h3><p>Download PDF certificates to print and physically hand them out or mail them to your customers!</p>
    </div>
    <div class="abs dist-item" style="left:128px">
      <svg viewBox="0 0 24 24" fill="#fff"><path d="M2 6h20v13H2z"/><path d="M2 6l10 8 10-8" fill="none" stroke="#0a4bd6" stroke-width="1.4"/></svg>
      <h3>Email</h3><p>Email e-certificates to your customers individually or in bulk with just one click! your closing question.</p>
    </div>
    <div class="abs dist-item" style="left:220px">
      <svg viewBox="0 0 24 24" fill="none" stroke="#fff" stroke-width="2"><rect x="2" y="3" width="20" height="13"/><path d="M12 16v4M7 21h10"/></svg>
      <h3>Online Automation</h3><p>Add our web banners on your website. Your customers click on the banner to get their certificate.</p>
    </div>
    <div class="abs dist-item" style="left:313px">
      <svg viewBox="0 0 24 24" fill="#fff"><path d="M2 3h20v14H9l-5 4v-4H2z"/><circle cx="8" cy="10" r="1.3" fill="#0a4bd6"/><circle cx="12" cy="10" r="1.3" fill="#0a4bd6"/><circle cx="16" cy="10" r="1.3" fill="#0a4bd6"/></svg>
      <h3>SMS</h3><p>Send one-certificates through text messaging with just one click! Coming Soon!</p>
    </div>
  </section>

  <section class="gift">
    <div class="abs gift-photo" role="img" aria-label="Dark gift box tied with a teal ribbon on a wooden table"></div>
    <div class="abs gift-copy">
      <h2>Give away an unlimited amount of certificates to your customers for just $99 bucks a month.</h2>
      <p class="small" style="margin-top:6px">We are A rated with the Regional Business Standards Council as well as a licensed seller of travel registered with the State Seller of Travel Registry (ST# 0000000). We also participate in The Traveler Protection Fund (TPF) which was created to protect consumers from unscrupulous travel companies.</p>
      <div style="position:relative;height:12px;margin-top:7px">
        <a class="btn btn-light" style="left:0;top:0;width:46px">Read More</a>
        <span class="abs link" style="left:55px;top:4px">Sign Up Risk free for 30 days now →</span>
      </div>
    </div>
  </section>

  <section class="cards">
    <div class="abs card" style="left:35px">
      <svg width="115" height="150" role="img" aria-label="Laptop on a desk"><rect width="115" height="150" fill="#3a3b3e"/><polygon points="0,82 115,50 115,150 0,150" fill="var(--blue)"/></svg>
      <div class="card-text" style="top:86px"><h3>Completely Separate Redemption Websites - Online Redemption/Reservation Requests</h3><p>First and foremost we're a marketing company and we will protect the integrity of your promotions. By using separate redemption websites keeps your customers from finding out what a great value you are getting.</p><p style="margin-top:3px">Read More →</p></div>
    </div>
    <div class="abs card" style="left:159px">
      <svg width="115" height="150" role="img" aria-label="Support agent wearing a headset"><rect width="115" height="150" fill="#4a4a4c"/><polygon points="0,140 115,96 115,150 0,150" fill="var(--blue)"/></svg>
      <div class="card-text" style="top:134px"><h3>Top Notch Customer Service With Superior Member Support</h3></div>
    </div>
    <div class="abs card" style="left:282px">
      <svg width="115" height="150" role="img" aria-label="Business people walking on a street"><rect width="115" height="150" fill="#505152"/><polygon points="0,140 115,96 115,150 0,150" fill="var(--blue)"/></svg>
      <div class="card-text" style="top:134px"><h3>Too good to be true! How Do We Do It?</h3></div>
    </div>
  </section>

  <section class="call">
    <div class="abs call-photo" role="img" aria-label="Red telephone handset"></div>
    <div class="abs call-copy">
      <h2>Increase your sales.<br>Improve your customer services.</h2>
      <div class="call-links"><span class="link">Watch video to save 20% today</span><span class="link">Take a quick tour to our incentives</span><span class="link">View Redeem Samples</span></div>
    </div>
  </section>

  <section class="reseller">
    <svg class="abs" style="left:0;top:0" width="431" height="70" role="img" aria-label="Team of colleagues meeting in an office"><polygon points="305,0 431,0 431,70 270,70" fill="#c9c3bd"/></svg>
    <div class="abs reseller-copy">
      <h2>Know Any Businesses That Could Benefit Using Incentives<br>To Bring In More Customers?</h2>
      <p class="link" style="margin-top:7px">Click Here To Learn More About Our Reseller Program</p>
    </div>
  </section>

  <footer class="site-footer">
    <div class="abs f-col" style="left:35px">Home<br>Our Incentives<br>Sample<br>How it works<br>Testimonials<br>FAQ<br>Contact</div>
    <div class="abs f-col" style="left:80px">Advertising<br>Residual Business<br>Sales<br>Referrals<br>Quick tour<br>Redeem Samples<br>Watch Video</div>
    <div class="abs f-col" style="left:134px">Download Brochure<br>Reseller Programs<br>Terms &amp; Conditions<br>Privacy Policy<br>Login</div>
    <div class="abs f-col" style="left:191px">Follow Us<br><span class="f-icon"></span>Social Page<br><span class="f-icon"></span>News Feed<br><span class="f-icon"></span>Video Channel</div>
    <div class="abs f-col" style="left:232px">Contact Us<br>&#9742; International: 1-800-555-0142<br>&nbsp;&nbsp;&nbsp;USA: 555-010-7731<br>&#9993; hello@brightlanepromoworks.biz<br>&nbsp;&nbsp;&nbsp;www.brightlanepromoworks.biz</div>
    <div class="abs f-col" style="left:327px;width:72px;line-height:7.6px">About Us<br>We are A rated with the Regional Business Standards Council as well as a licensed seller of travel registered with the State Registry (ST# 0000000). We also participate in the Traveler Fund.</div>
    <div class="abs copyright">© 2010-2018 Brightlane Promoworks Group, Inc. - All Rights Reserved. Affiliate Program</div>
  </footer>

</div>
</body>
</html>
```